New Book Cover for Website Advertising

I need a new book cover design to go on my website to generate pre-orders before my book is published. I have a previous design which I think needs a refresh. I want the new cover to complement the colours of my new website and logo. I'll attach the old book cover. All the words will remain the same, I just need an entirely new design

Target Market(s)

Corporate Leaders

Industry/Entity Type

Human resources

Font styles to use
Sans Serif

Colors
F0912C
F2A743
F7CA91
FBE8D2
FDF5EE
6B429C
8869AF
B7A5CE
E3DAEB
F3F0F8

Requirements
Must have
• A feeling of lightness, not dark
Should not have
• Any clip art or common stock photos

```html
<!DOCTYPE html>
<html lang="en">
<head>
<meta charset="utf-8">
<title>The Steady Mentor – Book Cover</title>
<link href="https://fonts.googleapis.com/css2?family=Bebas+Neue&family=Tinos:ital@0;1&display=swap" rel="stylesheet">
<style>
  :root {
    --backdrop: #e0e0e0;
    --cover-orange: #f2a743;
    --title-purple: #560c93;
    --title-white: #ffffff;
    --tagline-brown: #8a5518;
    --balloon-purple: #6b1fa0;
    --balloon-silver: #d4d4d4;
  }
  html, body {
    margin: 0;
    padding: 0;
    width: 853px;
    height: 1200px;
    overflow: hidden;
    background: var(--backdrop);
  }
  .canvas {
    position: relative;
    width: 853px;
    height: 1200px;
  }
  .book-cover {
    position: absolute;
    left: 46px;
    top: 30px;
    width: 760px;
    height: 1140px;
    background: var(--cover-orange);
    text-align: center;
  }
  .title {
    margin: 0;
    font-family: "Bebas Neue", "Arial Narrow", sans-serif;
    font-weight: 400;
  }
  .title span {
    position: absolute;
    left: 0;
    right: 0;
    display: block;
    line-height: 1;
    white-space: nowrap;
  }
  .title-the {
    top: 53px;
    font-size: 72px;
    color: var(--title-white);
  }
  .title-first {
    top: 135px;
    font-size: 160px;
    color: var(--title-purple);
  }
  .title-second {
    top: 288px;
    font-size: 160px;
    color: var(--title-white);
  }
  .balloons {
    position: absolute;
    left: 171px;
    top: 449px;
    width: 432px;
    height: 440px;
  }
  .tagline {
    position: absolute;
    left: 100px;
    right: 100px;
    top: 900px;
    margin: 0;
    font-family: "Tinos", "Times New Roman", serif;
    font-style: italic;
    font-size: 23px;
    line-height: 30px;
    color: var(--tagline-brown);
  }
  .author {
    position: absolute;
    left: 0;
    right: 0;
    top: 1000px;
    margin: 0;
    font-family: "Tinos", "Times New Roman", serif;
    font-size: 66px;
    line-height: 1.1;
    color: var(--title-white);
  }
</style>
</head>
<body>
<main class="canvas">
  <section class="book-cover">
    <h1 class="title">
      <span class="title-the">The</span>
      <span class="title-first">Steady</span>
      <span class="title-second">Mentor</span>
    </h1>
    <svg class="balloons" role="img" aria-label="Photograph of one purple balloon and two silver balloons floating on strings" viewBox="0 0 432 440">
      <defs>
        <linearGradient id="balloon-area" x1="0" y1="0" x2="1" y2="0">
          <stop offset="0" stop-color="var(--balloon-purple)" stop-opacity="0.35"/>
          <stop offset="0.4" stop-color="var(--balloon-silver)" stop-opacity="0.35"/>
          <stop offset="1" stop-color="var(--balloon-silver)" stop-opacity="0.35"/>
        </linearGradient>
      </defs>
      <rect width="432" height="440" fill="url(#balloon-area)"/>
    </svg>
    <p class="tagline">Learn how the way you form bonds shapes your connection with your colleagues, and their energy and results at work</p>
    <p class="author">Maren Holt</p>
  </section>
</main>
</body>
</html>
```